依頼概要
■依頼の目的/概要
当方、飲食店を4店舗経営しております
1.創作居酒屋
2.イタリアン+鮨
3.和食居酒屋
4.鮨+鉄板焼
以上4店舗です。
この度、新型コロナウイルスの影響で
お客様がご来店されなくなり
急遽、テイクアウトとデリバリーに力を
入れていこうと決めました。
そこで、魅力のあるメニューを作りたい
と考えております。
■要望のポイント
今回のメニューは先程あげました4店舗のメニューがそれぞれ入っております。
和と洋をイメージできるような、おしゃれな感じを望んでいます。お客様の層は幅広いですが、女性の方が多いです。
■その他注意点など
店内のイメージは
写真を送ることも可能ですが
菜ダイニング灯で検索していただけると
画像が出ると思います。
できればイメージの統一感があればいいなと思います。
メニューの内容や
写真はお送りいたします。
後ほど、写真の追加があります?
その他何かご不明点ただがあれば
お気軽にご質問ください
よろしくお願い致します
ロゴや料理写真を添付いたしました。
料理の写真は、店内メニュー用の写真なので
器とかが変わってしまいます。
ですので、このような料理です的なイメージみたいな感じでお願いできますでしょうか?
料理写真です。
宜しくお願いいたします。
ロゴです!
宜しくお願いいたします。
メニュー写真の追加です
全部の写真を使わなくても大丈夫です!
宜しくお願いいたします。
お弁当の写真です!
宜しくお願いいたします。
■ 選んだ理由

こちらの意向が伝わりやすく、イメージより良かったからです!!!

■ 提案者全員のお礼・コメント

毎月少しづつ内容やデザインを変えてやりたいと思っているので、またご縁があればうれしいなと思います!本当に素早いご対応ありがとうございます!

```html
<!DOCTYPE html>
<html lang="ja">
<head>
<meta charset="utf-8">
<title>菜ダイニング灯 テイクアウトメニュー</title>
<link href="https://fonts.googleapis.com/css2?family=Yuji+Boku&family=Noto+Sans+JP:wght@500;700;900&family=Noto+Serif+JP:wght@700;900&display=swap" rel="stylesheet">
<style>
:root{
  --red:#c8161d;
  --ink:#2a1a12;
  --cream:#fff8e8;
  --gold:#f2b51c;
  --orange:#e8731a;
  --line:#d9c9a8;
  --paper:#ffffff;
}
*{margin:0;padding:0;box-sizing:border-box}
html,body{width:846px;height:1200px;overflow:hidden;background:var(--paper)}
body{font-family:"Noto Sans JP",sans-serif;color:var(--ink);position:relative}
.block{position:absolute}
.photo{position:absolute;border-radius:4px}
.brush{font-family:"Yuji Boku",serif;color:var(--red);line-height:1}
.price{font-family:"Noto Serif JP",serif;font-weight:900;color:var(--red);white-space:nowrap}
.price small{font-size:.5em;margin-left:2px}
.tag{display:inline-block;background:var(--red);color:#fff;font-weight:700;font-size:13px;padding:1px 7px;border-radius:3px;margin-right:8px;line-height:1.5}

.pricebox{position:absolute;background:rgba(255,255,255,.94);padding:5px 12px 6px;border:2px solid var(--red)}
.pricebox .name{font-weight:900;font-size:14px;line-height:1.4}
.pricebox .row{display:flex;align-items:center;font-size:26px;line-height:1.2;margin-top:2px}

/* sashimi */
.sashimi{left:0;top:0;width:420px;height:318px}
.sashimi .photo{left:0;top:0;width:420px;height:318px;background:linear-gradient(135deg,#f08a6a,#e34a3a 45%,#f5d3b8 75%,#8a9b5c)}
.sashimi .title{position:absolute;left:14px;top:10px;font-size:60px;writing-mode:vertical-rl;background:rgba(255,255,255,.88);padding:8px 6px}
.sashimi .catch{position:absolute;left:100px;top:18px;font-weight:900;font-size:15px;color:#fff;text-shadow:0 1px 3px rgba(0,0,0,.6);line-height:1.4}
.sashimi .pricebox{left:16px;top:214px}

/* steak */
.steak{left:430px;top:0;width:416px;height:318px}
.steak .title{font-size:54px;position:absolute;left:8px;top:8px}
.steak .photo{left:0;top:70px;width:416px;height:132px;background:linear-gradient(120deg,#6b2a1c,#b9503a 50%,#e7a071)}
.steak .feature{position:absolute;right:10px;top:116px;text-align:right;background:rgba(255,255,255,.92);padding:3px 10px}
.steak .feature .name{font-weight:900;font-size:14px}
.steak .feature .price{font-size:28px;line-height:1.1}

.menu-list{list-style:none}
.menu-list li{display:flex;align-items:center;gap:6px;border-bottom:1px dotted var(--line);padding:2px 0;font-weight:700;font-size:15px;line-height:1.45}
.menu-list li .n{flex:1}
.menu-list li .price{font-size:20px}
.steak .menu-list{position:absolute;left:10px;right:10px;top:208px}
.steak .menu-list li .n small{font-size:11px}

/* sushi */
.sushi{left:0;top:326px;width:420px;height:230px}
.sushi .photo{left:0;top:0;width:420px;height:230px;background:linear-gradient(160deg,#3a2a22,#c85a3c 40%,#f2c4a0 70%,#e9e2d2)}
.sushi .title{position:absolute;left:14px;top:14px;font-size:56px;background:#fff;padding:6px 10px}
.sushi .catch{position:absolute;left:100px;top:22px;font-weight:900;font-size:15px;color:#fff;text-shadow:0 1px 3px rgba(0,0,0,.6)}
.sushi .pricebox{right:14px;top:82px}

/* curry */
.curry{left:430px;top:330px;width:416px;height:226px}
.curry .banner{background:var(--orange);color:#fff;font-weight:900;font-size:18px;text-align:center;padding:5px 0;border-radius:20px}
.curry .photo{left:0;top:46px;width:416px;height:132px;background:radial-gradient(circle at 55% 55%,#c87a22,#8a4a16 45%,#efe6d4 70%)}
.curry .feature{position:absolute;left:10px;right:10px;top:184px;display:flex;align-items:center;justify-content:space-between;font-weight:900;font-size:18px}
.curry .feature .price{font-size:30px}

/* sides */
.sides{left:18px;top:568px;width:810px;display:grid;grid-template-columns:1fr 1fr 1.15fr;column-gap:22px}
.sides .menu-list li{font-size:14px;min-height:33px}
.sides .menu-list li .n.long{font-size:11px;line-height:1.25}

/* pizza & pasta */
.pp-title{left:18px;top:686px;font-size:48px}
.pizza .photo{left:0;top:742px;width:420px;height:178px;background:radial-gradient(circle at 50% 55%,#e8b05a,#c8462a 40%,#6a3a1c 70%,#2a1a12)}
.pasta .banner{position:absolute;left:440px;top:694px;width:396px;background:var(--gold);color:var(--ink);font-weight:900;font-size:16px;text-align:center;padding:4px 0;border-radius:4px}
.pasta .photo{left:430px;top:730px;width:416px;height:190px;background:linear-gradient(140deg,#f3d9a4,#e2a04a 45%,#b8562c 80%)}
.pizza-list{left:18px;top:926px;width:400px}
.pasta-list{left:440px;top:926px;width:390px}
.pizza-list li,.pasta-list li{font-size:14px}

/* footer */
.footer{left:0;top:1094px;width:846px;height:106px;background:var(--cream);border-top:4px solid var(--red);display:flex;align-items:center;padding:0 18px;gap:16px}
.footer .place{font-size:12px;font-weight:700;line-height:1.5}
.footer .place .label{background:var(--ink);color:#fff;padding:1px 6px;font-size:11px}
.footer .shop{font-family:"Noto Serif JP",serif;font-weight:900;font-size:24px;display:flex;align-items:center;gap:8px;line-height:1.3}
.footer .shop .mark{width:13px;height:13px;background:var(--red);border-radius:50%}
.footer .right{margin-left:auto;text-align:right}
.footer .tel{display:flex;align-items:center;gap:6px;font-family:"Noto Serif JP",serif;font-weight:900;font-size:34px;color:var(--red);line-height:1}
.footer .hours{display:flex;align-items:center;gap:8px;justify-content:flex-end;margin-top:8px}
.footer .hours .label{background:var(--red);color:#fff;font-size:12px;font-weight:700;padding:2px 6px}
.footer .hours .time{font-weight:900;font-size:22px;line-height:1}
.footer .note{font-size:9px;color:#6a5a4a;margin-top:1px}
</style>
</head>
<body>

<section class="block sashimi">
  <div class="photo" role="img" aria-label="お刺身盛合わせの写真"></div>
  <h2 class="title brush">お刺身</h2>
  <p class="catch">その日のおすすめが<br>贅沢にいただける!!</p>
  <div class="pricebox">
    <p class="name">お刺身盛合わせ</p>
    <p class="row"><span class="tag">特上</span><span class="price">2,700<small>円</small></span></p>
    <p class="row"><span class="tag">上</span><span class="price">1,980<small>円</small></span></p>
  </div>
</section>

<section class="block steak">
  <h2 class="title brush">ステーキ</h2>
  <div class="photo" role="img" aria-label="黒毛和牛のステーキの写真"></div>
  <div class="feature"><p class="name">黒毛和牛のステーキ</p><p class="price">1,980<small>円</small></p></div>
  <ul class="menu-list">
    <li><span class="n">牛ステーキ丼</span><span class="price">2,200<small>円</small></span></li>
    <li><span class="n">鉄火丼</span><span class="price">1,350<small>円</small></span></li>
    <li><span class="n">おにぎり<small>（梅・鮭・明太子）</small></span><span class="price">各500<small>円</small></span></li>
  </ul>
</section>

<section class="block sushi">
  <div class="photo" role="img" aria-label="にぎり鮨の写真"></div>
  <h2 class="title brush">鮨</h2>
  <p class="catch">旬の鮮魚で本格にぎり鮨</p>
  <div class="pricebox">
    <p class="name">にぎり鮨</p>
    <p class="row"><span class="tag">特上</span><span class="price">2,980<small>円</small></span></p>
    <p class="row"><span class="tag">上</span><span class="price">1,850<small>円</small></span></p>
    <p class="row"><span class="tag">並</span><span class="price">1,450<small>円</small></span></p>
  </div>
</section>

<section class="block curry">
  <p class="banner">一度食べるとクセになる!</p>
  <div class="photo" role="img" aria-label="カレーライスの写真"></div>
  <p class="feature"><span>AKARIのカレーライス</span><span class="price">880<small>円</small></span></p>
</section>

<section class="block sides">
  <ul class="menu-list">
    <li><span class="n">玉子焼き5切れ</span><span class="price">450<small>円</small></span></li>
    <li><span class="n">クリームコロッケ</span><span class="price">550<small>円</small></span></li>
    <li><span class="n">天ぷら盛合わせ</span><span class="price">850<small>円</small></span></li>
  </ul>
  <ul class="menu-list">
    <li><span class="n">ポテトフライ</span><span class="price">550<small>円</small></span></li>
    <li><span class="n">地鶏の唐揚げAKARI風</span><span class="price">850<small>円</small></span></li>
    <li><span class="n">鶏から西京焼き</span><span class="price">1,080<small>円</small></span></li>
  </ul>
  <ul class="menu-list">
    <li><span class="n">枝豆</span><span class="price">550<small>円</small></span></li>
    <li><span class="n">ごぼうの唐揚げ</span><span class="price">550<small>円</small></span></li>
    <li><span class="n long">厚切りベーコンと<br>アボカドのシーザーサラダ</span><span class="price">980<small>円</small></span></li>
  </ul>
</section>

<h2 class="block pp-title brush">ピザ&amp;パスタ</h2>
<section class="pizza"><div class="photo" role="img" aria-label="窯焼きピザの写真"></div></section>
<section class="pasta">
  <p class="banner">お好きなパスタをいろいろありますよ♪</p>
  <div class="photo" role="img" aria-label="パスタの写真"></div>
</section>

<ul class="block menu-list pizza-list">
  <li><span class="n">マルゲリータ</span><span class="price">850<small>円</small></span></li>
  <li><span class="n">クアトロフォルマッジ</span><span class="price">1,280<small>円</small></span></li>
  <li><span class="n">粗挽きソーセージのスパイシーピザ</span><span class="price">1,080<small>円</small></span></li>
  <li><span class="n">フォアグラのRichピザ</span><span class="price">1,580<small>円</small></span></li>
</ul>
<ul class="block menu-list pasta-list">
  <li><span class="n">きのこのクリームパスタポルチーニソース</span><span class="price">1,400<small>円</small></span></li>
  <li><span class="n">HOT! HOT! アラビアータ</span><span class="price">980<small>円</small></span></li>
  <li><span class="n">明太子のクリームパスタ</span><span class="price">980<small>円</small></span></li>
  <li><span class="n">生ハムと大葉の七味ペペロンチーノ</span><span class="price">980<small>円</small></span></li>
  <li><span class="n">西京味噌と柚子胡椒のカルボナーラ</span><span class="price">1,080<small>円</small></span></li>
</ul>

<footer class="block footer">
  <div>
    <p class="place"><span class="label">受け取り場所</span></p>
    <p class="shop"><span class="mark"></span>菜ダイニング灯</p>
    <p class="place">〒030-0000 青森市中央3丁目2-8 灯ビル 1F</p>
    <p class="note">お支払い：現金・各種クレジット・スマホ決済もご利用いただけます</p>
  </div>
  <div class="right">
    <p class="tel">
      <svg width="28" height="28" viewBox="0 0 24 24" aria-hidden="true"><path fill="#c8161d" d="M6.6 10.8a15.1 15.1 0 0 0 6.6 6.6l2.2-2.2a1 1 0 0 1 1-.25 11.4 11.4 0 0 0 3.6.57 1 1 0 0 1 1 1V20a1 1 0 0 1-1 1A17 17 0 0 1 3 4a1 1 0 0 1 1-1h3.5a1 1 0 0 1 1 1c0 1.25.2 2.45.57 3.57a1 1 0 0 1-.25 1z"/></svg>
      017-640-4821
    </p>
    <p class="hours"><span class="label">お持ち帰り時間</span><span class="time">17:00～22:00</span></p>
  </div>
</footer>

</body>
</html>
```